Graphic design for "How It Works" for VelmoraStyles.com*

VelmoraStyles.com website is for selling custom designer outfits for women and girls in all countries, customers can choose existing designs on this website and customize to their measurements. Customers can also provide their own designs and measurements and our expert designers and tailors get the outfit stitched and delivered to the customer.

We wanted to explain how this entire process works in 4 steps in the form of graphic design with little heading and text describing each step.

Step 1: Select Dress
Its time to choose the beauty you want to adorn yourself with. We have a wide collection of premium dresses, colours and accessories. There is something for everyone! All you need to do is pick. If you can’t find what you are looking for then you can share a picture of what you want, we will get it done whatever you want.

Step 2: Customization
Everyone is different; hence we realise the need for customization of the design and size. Here you select exactly how you want your dress to be. From sleeves to cuts, everything will be done as per your wish. Enter your measurements, lo and behold! You’re done. Leave your comments for even more customization.

Step 3: Designer Consultation
We as a user-friendly brand, aspire to provide the best of services to our clients. Our expert lady designers will help you for everything right from selecting of fabric to design of dress to necessary accessories. Our designers are just a call away!

Step 4: Stitch and Deliver
After you have placed your order, we confirm and verify the details. The boutique completes your order, sends it to us and we deliver it to your doorstep. We also have a team of designers in-house to cater to your premium dressing needs.

```html
<!DOCTYPE html>
<html lang="en">
<head>
<meta charset="utf-8">
<title>How it works – VelmoraStyles.com</title>
<link rel="stylesheet" href="https://fonts.googleapis.com/css2?family=Montserrat:wght@400;600;700&display=swap">
<style>
  :root {
    --page-bg: #e6e6e6;
    --card-bg: #ffffff;
    --band: #3d3d3f;
    --title-pink: #c94a8a;
    --ink: #2b2b2b;
    --body-ink: #4a4a4a;
    --step-dark: #444446;
    --step-cyan: #1fd6e0;
    --step-green: #22ad1e;
    --step-orange: #f5a300;
    --connector: #8a8a8a;
    --dash: #b5b5b5;
    --art-light: #f3f3f3;
    --art-shade: #d6d6d6;
    --art-blue: #c9d3ee;
    --art-red: #f0c4c6;
    --art-purple: #cfc6e4;
  }
  * { margin: 0; padding: 0; box-sizing: border-box; }
  html, body {
    width: 1200px; height: 2357px; overflow: hidden;
    background: var(--page-bg);
    font-family: "Montserrat", sans-serif;
  }
  .process-card {
    position: absolute; left: 62px; top: 738px;
    width: 1076px; height: 880px;
    background: var(--card-bg);
    box-shadow: 0 4px 14px rgba(0,0,0,0.18);
  }
  .band { position: absolute; left: 0; width: 100%; background: var(--band); }
  .band--top { top: 0; height: 30px; }
  .band--bottom { bottom: 0; height: 20px; }
  .process-title {
    position: absolute; top: 58px; width: 100%;
    text-align: center; color: var(--title-pink);
    font-weight: 700; font-size: 56px; letter-spacing: 1px;
  }
  .process-diagram { position: absolute; left: 0; top: 0; }
  .step-label {
    position: absolute; width: 220px; margin-left: -110px;
    text-align: center; color: var(--ink);
    font-weight: 700; font-size: 19px; line-height: 20px;
  }
  .step-text {
    position: absolute; width: 208px;
    color: var(--body-ink); font-size: 12.2px; line-height: 15.4px;
    letter-spacing: -0.15px; word-spacing: -0.5px;
    text-align: justify;
  }
</style>
</head>
<body>
<main class="process-card">
  <div class="band band--top"></div>
  <h1 class="process-title">How it works</h1>

  <svg class="process-diagram" width="1076" height="880" viewBox="0 0 1076 880">
    <defs>
      <radialGradient id="artSelect" cx="50%" cy="42%" r="62%">
        <stop offset="0%" stop-color="var(--art-red)"/>
        <stop offset="35%" stop-color="var(--art-blue)"/>
        <stop offset="70%" stop-color="var(--art-light)"/>
        <stop offset="100%" stop-color="var(--art-shade)"/>
      </radialGradient>
      <radialGradient id="artCustom" cx="45%" cy="40%" r="62%">
        <stop offset="0%" stop-color="var(--art-blue)"/>
        <stop offset="40%" stop-color="var(--art-red)"/>
        <stop offset="72%" stop-color="var(--art-light)"/>
        <stop offset="100%" stop-color="var(--art-shade)"/>
      </radialGradient>
      <radialGradient id="artConsult" cx="50%" cy="50%" r="62%">
        <stop offset="0%" stop-color="var(--art-purple)"/>
        <stop offset="40%" stop-color="var(--art-blue)"/>
        <stop offset="72%" stop-color="var(--art-light)"/>
        <stop offset="100%" stop-color="var(--art-shade)"/>
      </radialGradient>
      <radialGradient id="artStitch" cx="50%" cy="48%" r="62%">
        <stop offset="0%" stop-color="#e8d2b8"/>
        <stop offset="40%" stop-color="var(--art-red)"/>
        <stop offset="72%" stop-color="var(--art-light)"/>
        <stop offset="100%" stop-color="var(--art-shade)"/>
      </radialGradient>
      <filter id="softShadow" x="-20%" y="-20%" width="140%" height="140%">
        <feDropShadow dx="0" dy="3" stdDeviation="3" flood-color="#000" flood-opacity="0.18"/>
      </filter>
    </defs>
    <g fill="none" stroke="var(--dash)" stroke-width="1.2" stroke-dasharray="3 3">
      <path d="M14 405 A175 175 0 0 1 300 405"/>
      <path d="M267 605 A175 175 0 0 0 553 605"/>
      <path d="M517 405 A175 175 0 0 1 803 405"/>
      <path d="M770 605 A175 175 0 0 0 1056 605"/>
    </g>
    <g fill="none" stroke-width="18">
      <path d="M24 505 A133 133 0 0 1 290 505" stroke="var(--step-dark)"/>
      <path d="M277 505 A133 133 0 0 0 543 505" stroke="var(--step-cyan)"/>
      <path d="M527 505 A133 133 0 0 1 793 505" stroke="var(--step-green)"/>
      <path d="M780 505 A133 133 0 0 0 1046 505" stroke="var(--step-orange)"/>
    </g>
    <g filter="url(#softShadow)">
      <circle cx="157" cy="505" r="114" fill="url(#artSelect)" role="img" aria-label="Illustration: online shop window with a red dress and cart button"/>
      <circle cx="410" cy="505" r="114" fill="url(#artCustom)" role="img" aria-label="Illustration: woman customising a dress on a website"/>
      <circle cx="660" cy="505" r="114" fill="url(#artConsult)" role="img" aria-label="Illustration: client and designer in a consultation meeting"/>
      <circle cx="913" cy="505" r="114" fill="url(#artStitch)" role="img" aria-label="Illustration: tailor stitching and courier delivering a parcel"/>
    </g>
    <g stroke="var(--connector)" stroke-width="2">
      <line x1="157" y1="248" x2="157" y2="330"/>
      <line x1="660" y1="246" x2="660" y2="330"/>
      <line x1="410" y1="680" x2="410" y2="730"/>
      <line x1="913" y1="680" x2="913" y2="732"/>
    </g>
    <g stroke="var(--connector)" stroke-width="4">
      <line x1="157" y1="300" x2="157" y2="330"/>
      <line x1="660" y1="300" x2="660" y2="330"/>
      <line x1="410" y1="680" x2="410" y2="708"/>
      <line x1="913" y1="680" x2="913" y2="710"/>
    </g>
    <g fill="#fff" stroke="var(--ink)" stroke-width="1.5">
      <circle cx="157" cy="248" r="6"/>
      <circle cx="660" cy="246" r="6"/>
      <circle cx="410" cy="730" r="6"/>
      <circle cx="913" cy="732" r="6"/>
    </g>
    <g fill="var(--ink)">
      <circle cx="157" cy="248" r="3"/>
      <circle cx="660" cy="246" r="3"/>
      <circle cx="410" cy="730" r="3"/>
      <circle cx="913" cy="732" r="3"/>
    </g>
  </svg>

  <h2 class="step-label" style="left:157px; top:210px;">Select Dress</h2>
  <h2 class="step-label" style="left:410px; top:748px;">Customization</h2>
  <h2 class="step-label" style="left:660px; top:190px;">Designer<br>Consultation</h2>
  <h2 class="step-label" style="left:913px; top:750px;">Stitch<br>and Deliver</h2>

  <p class="step-text" style="left:49px; top:653px;">Its time to choose the beauty you want to adorn yourself with. We have a wide collection of premium dresses, colours and accessories. There is something for everyone! All you need to do is pick. If you can’t find what you are looking for then you can share a picture of what you want, we will get it done whatever you want.</p>
  <p class="step-text" style="left:308px; top:182px;">Everyone is different; hence we realise the need for customization of the design and size. Here you select exactly how you want your dress to be. From sleeves to cuts, everything will be done as per your wish. Enter your measurements, lo and behold! You’re done. Leave your comments for even more customization.</p>
  <p class="step-text" style="left:559px; top:653px;">We as a user-friendly brand, aspire to provide the best of services to our clients. Our expert lady designers will help you for everything right from selecting of fabric to design of dress to necessary accessories. Our designers are just a call away!</p>
  <p class="step-text" style="left:819px; top:213px;">After you have placed your order, we confirm and verify the details. The boutique completes your order, sends it to us and we deliver it to your doorstep. We also have a team of designers in-house to cater to your premium dressing needs.</p>

  <div class="band band--bottom"></div>
</main>
</body>
</html>
```